Counseling Practice Business Card

I need a professional looking business card incorporating my new logo that was just completed. Card needs to incorporate my name and title, description of my specialty, my address, my phone number, my fax number, my email and my website URL. I need to be able to choose design on/with different paper colors and textures.
I do not have a lot of business card ideas so I am open to anything but I want bold,sharp, clear card without additional designs other than my logo (see attached file info). I am open to different color backgrounds or paper colors including black. I do not like traditional brackets around area codes in phone number or dashes between numbers in phone number. Am open to other ways of presenting including periods between numbers as appropriate. I do not know enough to know what I like yet but I want card to coordinate and work together with my logo. My practice emphasizes natural mental health interventions so any use of color (with background paper color or the blue and green in my logo) that elicits nature is nice. In addition to black, any natural brown or wood looking background might be desirable also. Most of the offerings so far look very similar and boring.

Target Market(s)

Potential therapy clients and other professionals

Contact Information for Business Card

Card information:
Marcus T. Whitfield, Ph.D.
Licensed Clinical Psychologist
Integrative Health Coach
4812 Ferndale Pkwy NW
Suite 730
Duluth, GA 30096
(770) 555-0142 phone
(770) 555-0186 fax
drmarcuswhitfield@kelvora.com
pathbloomcounseling.com

Font styles to use
Serif
Sans Serif
Other font styles liked:
• anything that you think looks crisp, clear and easily readable

Requirements
Must have
• Any color used should coordinate with my logo design (see attached files).
• Card should be printed horizontally so top and bottom are longest sides of rectangle.
• Background color or paper color should complement and highlight logo. Do not like a white background. black, grey, brown or any color my logo would blend well with.
Nice to have
• I would like designer to utilize color to highlight letters/name or phone-fax-web symbols.
• Bottom edge of card could be highlighted if appropriate to an idea.
Should not have
• I would NOT want the card to have a pure white background at all.
• No clear cards.
• Cards should be oriented with long sides on bottom and top, NOT sides. DO NOT LIKE THIS THIN TALL ORIENTATION.

```html
<!DOCTYPE html>
<html lang="en">
<head>
<meta charset="utf-8">
<title>Pathbloom Counseling – Business Card</title>
<link href="https://fonts.googleapis.com/css2?family=Lato:wght@400;700&display=swap" rel="stylesheet">
<style>
  :root {
    --page-bg: #e9e6e1;
    --card-deep: #0b2a86;
    --card-mid: #1446b8;
    --card-glow: #2f78d6;
    --panel-blue: #1b6fd3;
    --panel-dark: #262626;
    --name-blue: #3d8cf0;
    --ink-light: #e8f0ff;
    --rule: rgba(232, 240, 255, 0.85);
  }
  * { margin: 0; padding: 0; box-sizing: border-box; }
  html, body {
    width: 1200px; height: 1200px; overflow: hidden;
    background: var(--page-bg);
    font-family: "Lato", sans-serif;
  }
  .sheet {
    width: 1200px; height: 1200px;
    display: flex; flex-direction: column; align-items: center; justify-content: center;
    gap: 60px;
  }
  .card {
    position: relative;
    width: 900px; height: 514px;
    border-radius: 6px;
    overflow: hidden;
    box-shadow: 0 10px 30px rgba(0,0,0,0.25);
  }
  .card-texture {
    position: absolute; inset: 0;
    background:
      radial-gradient(ellipse at 45% 55%, var(--card-glow) 0%, transparent 55%),
      radial-gradient(ellipse at 85% 30%, rgba(47,120,214,0.5) 0%, transparent 45%),
      linear-gradient(135deg, var(--card-deep) 0%, var(--card-mid) 50%, var(--card-deep) 100%);
  }

  /* Back */
  .back-panel {
    position: absolute; right: 40px; top: 40px;
    width: 430px; height: 300px;
    background: var(--panel-dark);
    border-radius: 44px;
    display: flex; align-items: center; justify-content: center;
  }

  /* Brand name lockup */
  .brand {
    display: flex; align-items: center; gap: 14px;
    color: var(--ink-light);
    font-weight: 400;
  }
  .brand-dot {
    width: 26px; height: 26px; border-radius: 50%;
    background: var(--ink-light);
  }
  .brand-name {
    font-size: 40px; line-height: 1.15; letter-spacing: 1px;
  }
  .brand-name small {
    display: block; font-size: 18px; letter-spacing: 9px; text-transform: uppercase;
  }

  /* Front */
  .front-panel {
    position: absolute; left: 40px; top: 40px;
    width: 360px; height: 320px;
    background: var(--panel-blue);
    border-radius: 40px;
    display: flex; align-items: center; justify-content: center;
  }
  .front-panel .brand-name { font-size: 34px; }
  .front-panel .brand-name small { font-size: 15px; letter-spacing: 7px; }

  .identity {
    position: absolute; left: 440px; top: 52px; width: 420px;
    color: var(--ink-light);
  }
  .identity-name {
    color: var(--name-blue); font-weight: 700; font-size: 29px; margin-bottom: 8px;
  }
  .identity-title { font-size: 19px; line-height: 1.35; }
  .identity-rule {
    height: 2px; background: var(--rule); margin: 16px 0 22px;
  }
  .contact-list { list-style: none; }
  .contact-item {
    display: flex; align-items: center; gap: 16px;
    font-size: 18px; margin-bottom: 12px;
  }
  .contact-item.phone { font-size: 21px; }
  .contact-icon {
    width: 24px; height: 24px; flex: none;
  }
  .edge-tab {
    position: absolute; right: 0; top: 340px;
    width: 70px; height: 46px;
    background: var(--panel-blue);
    border-radius: 23px 0 0 23px;
    display: flex; align-items: center; padding-left: 12px;
  }
  .edge-tab span {
    width: 26px; height: 26px; border: 2px solid var(--ink-light); border-radius: 50%;
  }
  .address-band {
    position: absolute; left: 40px; right: 80px; top: 405px;
    border-top: 2px solid var(--rule);
    border-bottom: 2px solid var(--rule);
    padding: 18px 0 18px 44px;
    color: var(--ink-light);
    font-size: 22px; letter-spacing: 0.5px;
  }
</style>
</head>
<body>
<main class="sheet">

  <section class="card card-back" aria-label="Card back">
    <div class="card-texture" role="img" aria-label="Deep blue distressed paper texture"></div>
    <div class="back-panel">
      <div class="brand">
        <span class="brand-dot"></span>
        <span class="brand-name">Pathbloom<small>Counseling</small></span>
      </div>
    </div>
  </section>

  <section class="card card-front" aria-label="Card front">
    <div class="card-texture" role="img" aria-label="Deep blue distressed paper texture"></div>

    <div class="front-panel">
      <div class="brand">
        <span class="brand-dot"></span>
        <span class="brand-name">Pathbloom<small>Counseling</small></span>
      </div>
    </div>

    <div class="identity">
      <h1 class="identity-name">Marcus T. Whitfield, Ph.D.</h1>
      <p class="identity-title">Licensed Clinical Psychologist<br>Integrative Health Coach</p>
      <div class="identity-rule"></div>
      <ul class="contact-list">
        <li class="contact-item phone">
          <svg class="contact-icon" viewBox="0 0 24 24" fill="none" stroke="#e8f0ff" stroke-width="1.5"><circle cx="12" cy="12" r="11"/><path d="M8 7l2 0 1 3-1.5 1a6 6 0 0 0 3.5 3.5l1-1.5 3 1v2a1 1 0 0 1-1 1A9 9 0 0 1 7 8a1 1 0 0 1 1-1z"/></svg>
          (770) 555-0142
        </li>
        <li class="contact-item phone">
          <svg class="contact-icon" viewBox="0 0 24 24" fill="none" stroke="#e8f0ff" stroke-width="1.5"><circle cx="12" cy="12" r="11"/><rect x="6" y="10" width="12" height="7" rx="1"/><path d="M8 10V6h8v4M9 13h6"/></svg>
          (770) 555-0186
        </li>
        <li class="contact-item">
          <svg class="contact-icon" viewBox="0 0 24 24" fill="none" stroke="#e8f0ff" stroke-width="1.5"><circle cx="12" cy="12" r="11"/><circle cx="12" cy="12" r="6"/><path d="M6 12h12M12 6c-2.5 3-2.5 9 0 12M12 6c2.5 3 2.5 9 0 12"/></svg>
          pathbloomcounseling.com
        </li>
        <li class="contact-item">
          <svg class="contact-icon" viewBox="0 0 24 24" fill="none" stroke="#e8f0ff" stroke-width="1.5"><circle cx="12" cy="12" r="11"/><rect x="6" y="8" width="12" height="8" rx="1"/><path d="M6 8l6 5 6-5"/></svg>
          drmarcuswhitfield@kelvora.com
        </li>
      </ul>
    </div>

    <div class="edge-tab"><span></span></div>

    <p class="address-band">4812 Ferndale Pkwy NW, Suite 730, Duluth, GA 30096</p>
  </section>

</main>
</body>
</html>
```